International Medical travel company needs professional card

We just purchased a logo through craft lantern, and now need a business card. We contract with Middle Eastern governments to bring patients who need complex medical care to the U.S. for treatment. We will upload logo. Titles, names, contact info, etc. needs to be in English on one side, Arabic on the other

Target Market(s)

Health administrators, professionals

Industry/Entity Type

Health Care

Contact Information for Business Card

logo on each side. Usual name/title/contact info

Font styles to use
Serif
Sans Serif

Colors
0255a3

Requirements
Must have
• English one side, Arabic the other

```html
<!DOCTYPE html>
<html lang="en">
<head>
<meta charset="utf-8">
<title>Meridian Care – Business Card</title>
<link href="https://fonts.googleapis.com/css2?family=Open+Sans:wght@400&display=swap" rel="stylesheet">
<style>
  :root {
    --backdrop: #3b3b3b;
    --card: #ffffff;
    --brand-blue: #0255a3;
    --brand-gold: #9a9118;
    --body-text: #555555;
  }
  html, body {
    margin: 0;
    padding: 0;
    width: 1105px;
    height: 1200px;
    overflow: hidden;
    background: var(--backdrop);
    font-family: "Open Sans", Arial, sans-serif;
  }
  .business-card {
    position: absolute;
    left: 52px;
    top: 314px;
    width: 1000px;
    height: 571px;
    background: var(--card);
  }
  .brand-mark {
    position: absolute;
    left: 733px;
    top: 54px;
    width: 140px;
    height: 140px;
    box-sizing: border-box;
    border: 6px solid var(--brand-gold);
  }
  .brand-name {
    position: absolute;
    left: 603px;
    top: 212px;
    width: 404px;
    text-align: center;
    margin: 0;
    font-size: 44px;
    font-weight: 400;
    letter-spacing: 1px;
    color: var(--brand-gold);
  }
  .person-name {
    position: absolute;
    left: 50px;
    top: 250px;
    margin: 0;
    font-size: 38px;
    font-weight: 400;
    color: var(--brand-blue);
  }
  .person-title {
    position: absolute;
    left: 50px;
    top: 291px;
    margin: 0;
    font-size: 25px;
    font-weight: 400;
    color: var(--brand-gold);
  }
  .contact-list {
    position: absolute;
    left: 50px;
    top: 338px;
    margin: 0;
    padding: 0;
    list-style: none;
  }
  .contact-item {
    display: flex;
    align-items: center;
    height: 38.5px;
    font-size: 26px;
    color: var(--body-text);
  }
  .contact-icon {
    width: 26px;
    height: 26px;
    margin-right: 14px;
    fill: var(--brand-blue);
  }
  .postal-address {
    position: absolute;
    left: 412px;
    top: 420px;
    font-style: normal;
    font-size: 26px;
    line-height: 35px;
    color: var(--body-text);
  }
</style>
</head>
<body>
  <section class="business-card">
    <div class="brand-mark" aria-hidden="true"></div>
    <p class="brand-name">MERIDIAN CARE</p>

    <h1 class="person-name">OMAR HADDAD</h1>
    <p class="person-title">CEO/FOUNDER</p>

    <ul class="contact-list">
      <li class="contact-item">
        <svg class="contact-icon" viewBox="0 0 24 24" aria-label="Phone"><path d="M6.6 10.8a15.1 15.1 0 0 0 6.6 6.6l2.2-2.2a1 1 0 0 1 1-.25 11.4 11.4 0 0 0 3.6.57 1 1 0 0 1 1 1V20a1 1 0 0 1-1 1A17 17 0 0 1 3 4a1 1 0 0 1 1-1h3.5a1 1 0 0 1 1 1c0 1.25.2 2.45.57 3.57a1 1 0 0 1-.25 1z"/></svg>
        512 304 7716
      </li>
      <li class="contact-item">
        <svg class="contact-icon" viewBox="0 0 24 24" aria-label="Mobile"><path d="M7 1h10a2 2 0 0 1 2 2v18a2 2 0 0 1-2 2H7a2 2 0 0 1-2-2V3a2 2 0 0 1 2-2zm0 3v14h10V4zm5 15.5a1.2 1.2 0 1 0 0 2.4 1.2 1.2 0 0 0 0-2.4z"/></svg>
        741 219 5830
      </li>
      <li class="contact-item">
        <svg class="contact-icon" viewBox="0 0 24 24" aria-label="Fax"><path d="M6 2h9l3 3v4H6zM3 10h18a1 1 0 0 1 1 1v8a1 1 0 0 1-1 1H3a1 1 0 0 1-1-1v-8a1 1 0 0 1 1-1zm3 4v2h12v-2z"/></svg>
        603 582 4197
      </li>
      <li class="contact-item">
        <svg class="contact-icon" viewBox="0 0 24 24" aria-label="Email"><path d="M2 5h20v14H2zm2 2v.5l8 5 8-5V7z"/></svg>
        omar@meridiancare.org
      </li>
      <li class="contact-item">
        <svg class="contact-icon" viewBox="0 0 24 24" aria-label="Website"><path d="M12 2a10 10 0 1 0 0 20 10 10 0 0 0 0-20zm-1 17.9A8 8 0 0 1 4.1 10.9L9 15.5v1.5a2 2 0 0 0 2 2zm6.9-2.5A2 2 0 0 0 16 16h-1v-3a1 1 0 0 0-1-1H8v-2h2a1 1 0 0 0 1-1V7h2a2 2 0 0 0 2-2v-.4a8 8 0 0 1 2.9 12.8z"/></svg>
        www.meridiancare.org
      </li>
    </ul>

    <address class="postal-address">
      4120 Willow Creek Road<br>
      Fairbanks<br>
      Alaska 99712
    </address>
  </section>
</body>
</html>
```